Speisekarten-Design für Gastronomiebetrieb
Zielgruppe
Wir sind ein Gastronomiebetrieb in einer Studentenstadt. Unsere Hauptzielgruppe sind junge Menschen und Studenten, aber auch älteres Puplikum. Wir möchten gerne ein neues Speisekartendesign, da unser aktuelles seit über 10 Jahren sich kaum verändert hat.
Aufgabenstellung
Gerne könne Sie sich die aktulle Speisekarte auf der unserer Hompeage anschauen: www.tomello-kassel.de
Auf der Frontseite soll die Farbrichtung Orange und natürlich das Logo beibehalten werden. Für die restlichen Seiten gibt es diese Einschränkung nicht. Uns ist wichtig, dass die Speisekarte modern, bunt und peppig ist. Das heisst möglichst mit kräftigen Farben und Bildern von Speisen und Getränken arbeiten.

```html
<!DOCTYPE html>
<html lang="de">
<head>
<meta charset="utf-8">
<title>Speisekarte – Suppen, Snacks und Burger</title>
<link rel="stylesheet" href="https://fonts.googleapis.com/css2?family=Oswald:wght@400;500&family=Source+Sans+3:wght@500;600&display=swap">
<style>
  :root {
    --backdrop: #e7e7e7;
    --paper-orange: #f19a25;
    --paper-orange-deep: #e98f1c;
    --header-red: #e9402a;
    --title-red: #e2331f;
    --text-white: #ffffff;
    --rule-white: rgba(255, 255, 255, 0.85);
    --frame-white: #f2f2f2;
  }
  * { box-sizing: border-box; margin: 0; padding: 0; }
  html, body { width: 1200px; height: 900px; overflow: hidden; background: var(--backdrop); }
  body { position: relative; font-family: "Source Sans 3", "Helvetica Neue", Arial, sans-serif; }

  .spread {
    position: absolute; left: 20px; top: 149px; width: 1160px; height: 602px;
    display: flex; box-shadow: 0 14px 30px rgba(0,0,0,0.18);
  }
  .page {
    position: relative; height: 100%; overflow: hidden;
    background: radial-gradient(ellipse at 40% 40%, var(--paper-orange), var(--paper-orange-deep));
    color: var(--text-white);
  }
  .page--left { width: 565px; }
  .page--right { width: 595px; }
  .page--left::after, .page--right::before {
    content: ""; position: absolute; top: 0; bottom: 0; width: 26px; pointer-events: none;
  }
  .page--left::after { right: 0; background: linear-gradient(to right, rgba(0,0,0,0), rgba(0,0,0,0.12)); }
  .page--right::before { left: 0; background: linear-gradient(to left, rgba(0,0,0,0), rgba(0,0,0,0.1)); z-index: 1; }

  .section-banner { position: absolute; left: 0; top: 0; }
  .section-title {
    position: absolute; left: 35px; top: 32px;
    font-family: "Oswald", "Arial Narrow", sans-serif; font-weight: 500;
    font-size: 23px; line-height: 23px; letter-spacing: 0.5px; text-transform: uppercase;
    color: var(--text-white);
  }

  .item { position: absolute; }
  .item-head {
    display: flex; justify-content: space-between; align-items: baseline;
    font-family: "Oswald", "Arial Narrow", sans-serif; font-weight: 400;
    font-size: 15px; line-height: 18px; color: var(--title-red); text-transform: uppercase;
    white-space: nowrap;
  }
  .item-desc { font-size: 10.5px; line-height: 15px; font-weight: 600; color: var(--text-white); }
  .item-desc sup { font-size: 6px; line-height: 0; vertical-align: super; }
  .item-row { display: flex; justify-content: space-between; align-items: flex-start; }
  .price-inline {
    font-family: "Oswald", "Arial Narrow", sans-serif; font-size: 15px; line-height: 15px;
    color: var(--title-red); white-space: nowrap; margin-top: -1px;
  }

  .rule { position: absolute; height: 1px; background: var(--rule-white); }
  .rule--bold { height: 4px; background: var(--text-white); }
  .column-divider { position: absolute; width: 1.5px; background: var(--title-red); }

  .note {
    position: absolute; font-family: "Oswald", "Arial Narrow", sans-serif; font-weight: 400;
    font-size: 10.5px; line-height: 16px; text-transform: uppercase; color: var(--text-white);
    letter-spacing: 0.3px;
  }

  .photo {
    position: absolute; background: var(--frame-white); padding: 9px 9px 12px;
    box-shadow: 0 4px 10px rgba(0,0,0,0.25); z-index: 2;
  }
  .photo-fill { width: 100%; height: 100%; }
  .photo--burger-top { left: 384px; top: -6px; width: 180px; height: 168px; transform: rotate(3deg); }
  .photo--burger-top .photo-fill { background: linear-gradient(160deg, #e2c9a0, #c98a3c 45%, #6b8f3a 70%, #5a3a22); }
  .photo--burger-main { left: 352px; top: 160px; width: 232px; height: 262px; transform: rotate(-12deg); }
  .photo--burger-main .photo-fill { background: linear-gradient(170deg, #f3ead4, #e0a14a 35%, #6aa63a 55%, #5b3a23 70%, #c99458); }
  .photo--fries { left: 332px; top: 442px; width: 194px; height: 180px; transform: rotate(2deg); }
  .photo--fries .photo-fill { background: linear-gradient(150deg, #f6d77a, #e9b443 50%, #c78a2a); }
</style>
</head>
<body>
  <main class="spread">
    <section class="page page--left">
      <svg class="section-banner" width="230" height="125" viewBox="0 0 230 125" aria-hidden="true">
        <polygon points="0,0 214,0 222,91 0,120" fill="var(--header-red)"/>
      </svg>
      <h2 class="section-title">Suppen<br>und Snacks</h2>

      <div class="item" style="left:36px; top:129px; width:243px;">
        <div class="item-head"><span>Tomatensuppe</span><span>3,90 €</span></div>
      </div>
      <div class="rule" style="left:36px; top:153px; width:247px;"></div>
      <div class="item" style="left:36px; top:159px; width:243px;">
        <div class="item-head"><span>Broccolicremesuppe</span><span>3,90 €</span></div>
      </div>
      <div class="rule" style="left:36px; top:184px; width:247px;"></div>
      <div class="item" style="left:36px; top:190px; width:243px;">
        <div class="item-head"><span>Hühnersuppe</span><span>3,90 €</span></div>
      </div>
      <div class="rule" style="left:36px; top:215px; width:247px;"></div>
      <p class="note" style="left:36px; top:224px; width:247px;">Alle Suppen werden mit ofenfrischen<br>Pizzabrötchen serviert.</p>
      <div class="rule rule--bold" style="left:36px; top:264px; width:247px;"></div>

      <div class="item" style="left:36px; top:282px; width:243px;">
        <div class="item-head"><span>Bruschetta Classico Italiano</span><span>5,50 €</span></div>
        <p class="item-desc">mit Schafskäse<sup>16</sup>, Tomaten und<br>Knoblauch, dazu Salat</p>
      </div>
      <div class="rule" style="left:36px; top:342px; width:247px;"></div>

      <div class="item" style="left:36px; top:358px; width:243px;">
        <div class="item-head"><span>Tortilla Vega</span><span>7,50 €</span></div>
        <p class="item-desc">gefüllter Wrap mit Champignons,<br>Zwiebeln, Paprika, Tomaten, Mais und<br>Schafskäse<sup>16</sup> in Tomatensoße mit Käse<sup>1,2,16</sup><br>überbacken, dazu Salat</p>
      </div>
      <div class="rule" style="left:36px; top:449px; width:247px;"></div>

      <div class="item" style="left:36px; top:464px; width:243px;">
        <div class="item-head"><span>Tortilla Hähnchen</span><span>8,50 €</span></div>
        <p class="item-desc">gefüllter Wrap mit gegrillter Hähnchen-<br>brust, Champignons, Zwiebeln, Paprika,<br>Tomaten, Mais und Schafskäse<sup>16</sup> in<br>Tomatensoße mit Käse<sup>1,2,16</sup> überbacken,<br>dazu Salat</p>
      </div>

      <div class="column-divider" style="left:297px; top:127px; height:424px;"></div>

      <div class="item" style="left:314px; top:129px; width:225px;">
        <div class="item-head"><span>Gebackener Schafskäse</span><span>6,90 €</span></div>
        <p class="item-desc">mit Preiselbeeren, dazu Salat und Brot</p>
      </div>
      <div class="rule" style="left:314px; top:176px; width:225px;"></div>

      <div class="item" style="left:314px; top:190px; width:225px;">
        <div class="item-head"><span>Ofenkartoffel</span></div>
        <div class="item-row"><p class="item-desc">mit Sauerrahm und Salat</p><span class="price-inline">6,90 €</span></div>
      </div>
      <div class="rule" style="left:314px; top:237px; width:225px;"></div>

      <div class="item" style="left:314px; top:251px; width:225px;">
        <div class="item-head"><span>Ofenkartoffel Verdure</span></div>
        <div class="item-row"><p class="item-desc">mit gebratenem Gemüse, dazu<br>Sauerrahm und Salat</p><span class="price-inline">7,80 €</span></div>
      </div>
      <div class="rule" style="left:314px; top:314px; width:225px;"></div>

      <div class="item" style="left:314px; top:327px; width:225px;">
        <div class="item-head"><span>Ofenkartoffel Polo (scharf)</span></div>
        <div class="item-row"><p class="item-desc">mit gebratenem Gemüse, Hähnchenbrust-<br>streifen, dazu Sauerrahm und Salat</p><span class="price-inline">8,90 €</span></div>
      </div>
      <div class="rule" style="left:314px; top:390px; width:225px;"></div>

      <div class="item" style="left:314px; top:403px; width:225px;">
        <div class="item-head"><span>Gebackener Camembert</span></div>
        <div class="item-row"><p class="item-desc">mit Preiselbeeren, dazu Salat und Brot</p><span class="price-inline">6,90 €</span></div>
      </div>
      <div class="rule" style="left:314px; top:451px; width:225px;"></div>

      <div class="item" style="left:314px; top:464px; width:225px;">
        <div class="item-head"><span>Taco Chips</span></div>
        <div class="item-row"><p class="item-desc">überbacken mit Käse<sup>1,2,16</sup>, dazu Salsa</p><span class="price-inline">4,50 €</span></div>
      </div>
      <div class="rule" style="left:314px; top:514px; width:225px;"></div>

      <div class="item" style="left:314px; top:525px; width:225px;">
        <div class="item-head"><span>Pommes Frites</span></div>
        <div class="item-row"><p class="item-desc">mit Ketchup oder Mayonnaise</p><span class="price-inline">3,50 €</span></div>
      </div>
    </section>

    <section class="page page--right">
      <svg class="section-banner" width="230" height="125" viewBox="0 0 230 125" aria-hidden="true">
        <polygon points="0,0 210,0 220,91 0,120" fill="var(--header-red)"/>
      </svg>
      <h2 class="section-title" style="top:36px;">Burger</h2>

      <div class="item" style="left:35px; top:129px; width:241px;">
        <div class="item-head"><span>Tomello Burger</span><span>8,50 €</span></div>
        <p class="item-desc">mit knackigen Salatblättern,<br>Tomaten, Zwiebeln, Gewürzgurken<br>und Cocktailsoße</p>
      </div>
      <div class="rule" style="left:35px; top:207px; width:245px;"></div>

      <div class="item" style="left:35px; top:220px; width:241px;">
        <div class="item-head"><span>Chiliburger</span><span>8,90 €</span></div>
        <p class="item-desc">mit knackigen Salatblättern, Tomaten,<br>Zwiebeln, Gewürzgurken, Käse<sup>1,2,16</sup>,<br>Jalapeños, Bacon<sup>2,3,7,Hs</sup> und Chilisauce<br>gemischt mit Cocktailsauce</p>
      </div>
      <div class="rule" style="left:35px; top:313px; width:245px;"></div>

      <div class="item" style="left:35px; top:327px; width:241px;">
        <div class="item-head"><span>BBQ-Burger</span><span>8,90 €</span></div>
        <p class="item-desc">mit knackigen Salatblättern, Tomaten,<br>Zwiebeln, Mayonnaise, Gewürzgurken,<br>Käse<sup>1,2,16</sup> und BBQ-Soße</p>
      </div>
      <div class="rule" style="left:35px; top:405px; width:245px;"></div>

      <p class="note" style="left:35px; top:418px; width:245px;">Unsere Burger werden mit 100 % Rind-<br>fleisch zubereitet und mit Pommes Frites<br>und Salat serviert.</p>
      <div class="rule rule--bold" style="left:35px; top:476px; width:245px;"></div>

      <figure class="photo photo--burger-top"><div class="photo-fill" role="img" aria-label="Foto: Burger mit Sesambrötchen, Bacon, Salat und Käse"></div></figure>
      <figure class="photo photo--burger-main"><div class="photo-fill" role="img" aria-label="Foto: Cheeseburger mit Salat und Tomate auf Holzbrett, Pommes im Hintergrund"></div></figure>
      <figure class="photo photo--fries"><div class="photo-fill" role="img" aria-label="Foto: Pommes Frites in Nahaufnahme"></div></figure>
    </section>
  </main>
</body>
</html>
```